House Building & Development Guide

e-guide, lead magnet to walk land owners through the potential costs in a building project. To be used as a tool to gather quotes and be useful while promoting our Building company and Investment company in case we can work with them or buy their land. Images to use and logo designs can be accessed via: https://files.storevault-example.net/shared/48QX2-_PbTRweHvLs61k9mmTfaPWzqRjc?mode=view website at www.harbourlineestates.co.uk

Target Market(s)

land owners

Industry/Entity Type

Construction Company

Font styles to use
Other font styles liked:
• Try to match or construction company branding www.harbourlinebuilders.co.uk

Requirements
Must have
• Be useful to 'use'
• Use our brand colours yellow #F3D324 blue #22384D
Nice to have
• Well balanced use of our best images
Should not have
• cluttered or unfriendly

```html
<!DOCTYPE html>
<html lang="en">
<head>
<meta charset="utf-8">
<title>Harbourline – House Building &amp; Development Cost Guide</title>
<link rel="stylesheet" href="https://fonts.googleapis.com/css2?family=Oswald:wght@500;700&family=Lato:wght@400;700;900&display=swap">
<style>
:root{
  --yellow:#f3d324;
  --navy:#22384d;
  --board:#e3e3e3;
  --paper:#ffffff;
  --ink:#2a2a2a;
  --muted:#555b61;
  --head:"Oswald",Impact,sans-serif;
  --body:"Lato",Arial,sans-serif;
}
*{box-sizing:border-box;margin:0;padding:0}
html,body{width:1200px;height:900px;overflow:hidden}
body{background:var(--board);font-family:var(--body);color:var(--ink);position:relative}
.page{position:absolute;top:222px;width:250px;height:354px;overflow:hidden;background:var(--paper);box-shadow:0 2px 6px rgba(0,0,0,.18)}
.page--cover{left:62px}
.page--inner1{left:345px}
.page--inner2{left:610px}
.page--back{left:880px;background:var(--navy)}
.caption{position:absolute;top:590px;width:250px;text-align:center;font:700 15px var(--body);color:#2b2b2b;letter-spacing:.2px}
.abs{position:absolute}

/* brand */
.brand{display:flex;align-items:center;gap:6px}
.brand__mark{width:20px;height:20px;background:var(--yellow)}
.brand__name{font:900 13px var(--body);color:var(--navy);line-height:1}

/* cover */
.cover__sky{left:0;top:0;width:250px;height:80px;background:linear-gradient(#ffffff 0%,#eef3f8 55%,#d6e4f0 100%)}
.cover__photo{left:0;top:80px;width:250px;height:145px;background:linear-gradient(#cddff0 0%,#b9cbb0 35%,#7f8b5a 55%,#8d7555 78%,#6c5642 100%)}
.cover__band{left:0;top:225px;width:250px;height:101px;background:var(--navy)}
.cover__frame{left:28px;top:78px;width:192px;height:206px;border:2.5px solid var(--yellow)}
.cover__sub{left:0;width:250px;top:252px;text-align:center;font:700 8px var(--body);color:var(--yellow)}
.cover__title{left:0;width:250px;top:264px;text-align:center;font:700 12.5px var(--head);color:#fff;letter-spacing:.3px}
.cover__blurb{left:8px;width:234px;top:296px;font:400 4.2px/1.4 var(--body);color:#dfe6ee}
.cover__call{left:0;width:250px;top:330px;text-align:center;font:900 10px var(--body);color:var(--navy)}
.footer{left:0;top:343px;width:250px;height:11px;background:var(--yellow);font:700 4.5px/11px var(--body);text-align:center;color:var(--navy);letter-spacing:.4px}

/* inner */
.title-row{left:12px;top:14px;display:flex;gap:4px}
.title-row span{font:700 15px/20px var(--head);padding:0 5px}
.title-row .t1{background:var(--yellow);color:var(--navy)}
.title-row .t2{background:var(--navy);color:#fff}
.intro{left:12px;top:40px;width:225px;font:700 5px/1.35 var(--body);color:var(--navy)}
.col{position:absolute;display:flex;flex-direction:column;gap:7px;width:112px}
.item h3{font:900 4.8px var(--body);color:var(--navy);border-bottom:1.5px solid var(--yellow);padding:1.5px 3px;background:#f4f4f4;margin-bottom:2px}
.item p{font:400 3.6px/1.4 var(--body);color:var(--muted);padding:0 2px;margin-bottom:2.5px}
.cost{display:table;background:var(--yellow);color:var(--navy);font:900 4.2px/1.3 var(--body);padding:1.5px 3px;max-width:100%}
.cost--navy{background:var(--navy);color:#fff}
.inner1__photo{left:140px;top:274px;width:108px;height:78px;background:linear-gradient(#ffffff,#e8e4d0 45%,#d7b62e 72%,#5c5a52 100%)}
.inner1__brand{left:142px;top:262px}
.inner1__brand .brand__mark{width:7px;height:7px}
.inner1__brand .brand__name{font-size:5.5px}
.inner2__photo{left:0;top:0;width:250px;height:66px;background:linear-gradient(#b8c7a8,#7b8c5c 45%,#b89a2c 70%,#5a5446 100%)}
.section-tag{display:inline-block;background:var(--navy);color:#fff;font:700 7px var(--head);padding:1px 8px}

/* back */
.back__frame{left:30px;top:76px;width:192px;height:206px;border:2.5px solid var(--yellow)}
.back__lead{left:36px;width:180px;top:122px;text-align:center;font:700 5.6px/1.35 var(--body);color:#fff}
.back__name{left:0;width:250px;top:138px;text-align:center;font:700 18px var(--head);color:#fff}
.back__phone{left:0;width:250px;top:160px;text-align:center;font:700 19px var(--head);color:var(--yellow)}
.back__mail{left:50px;width:150px;top:187px;background:#fff;text-align:center;font:700 6px/11px var(--body);color:var(--navy)}
.back__web{left:0;width:250px;top:214px;text-align:center;font:700 5px var(--body);color:#fff;letter-spacing:.6px}
.back__brand{left:48px;top:246px}
.back__brand .brand__name{color:#fff}
</style>
</head>
<body>

<!-- COVER -->
<section class="page page--cover">
  <div class="abs cover__sky"></div>
  <div class="abs cover__photo" role="img" aria-label="Orange excavator digging foundations on a building plot under a blue sky"></div>
  <div class="abs brand" style="left:40px;top:28px">
    <div class="brand__mark"></div>
    <div class="brand__name">HARBOURLINE BUILDERS</div>
  </div>
  <div class="abs cover__band"></div>
  <div class="abs cover__frame"></div>
  <div class="abs cover__sub">Harbourline Property Group House Building</div>
  <div class="abs cover__title">&amp; DEVELOPMENT COST GUIDE</div>
  <p class="abs cover__blurb">House Building &amp; Development Guide – a simple list of the typical costs you may face on a project, from buying land to the final finish.</p>
  <div class="abs cover__call">CALL US- 07700 900418</div>
  <div class="abs footer">www.harbourlinebuilders.co.uk</div>
</section>

<!-- INNER PAGE 1 -->
<section class="page page--inner1">
  <div class="abs title-row"><span class="t1">PRE BUILD COSTS</span><span class="t2">LAND COST</span></div>
  <p class="abs intro">Whether you're buying land with or without planning or buying a building to knock down and start again the cost of land is the biggest cost consideration for your project.</p>
  <div class="col" style="left:8px;top:62px">
    <div class="item"><h3>LAND VALUATION</h3><p>Budget for this item early, compare at least two written quotes and agree the scope in writing before any work begins on site.</p><span class="cost">EXPECTED COST: £400 - £1000</span></div>
    <div class="item"><h3>STAMP DUTY LAND TAX OR SDLT</h3><p>Budget for this item early, compare at least two written quotes and agree the scope in writing before any work begins on site.</p><span class="cost">THE COST WILL BE A PERCENTAGE OF THE VALUE</span></div>
    <div class="item"><h3>ARCHITECTS &amp; PLANNING DRAWINGS</h3><p>Budget for this item early, compare at least two written quotes and agree the scope in writing before any work begins on site.</p><span class="cost">EXPECTED COST: £1000 - £3000</span></div>
    <div class="item"><h3>PARTY WALL AGREEMENTS</h3><p>Budget for this item early, compare at least two written quotes and agree the scope in writing before any work begins on site.</p><span class="cost">EXPECTED COST: £0 - IF SERVING NOTICES YOURSELF</span></div>
    <div class="item"><h3>ADDITIONAL INSURANCES</h3><p>Budget for this item early, compare at least two written quotes and agree the scope in writing before any work begins on site.</p><span class="cost">EXPECTED COST: £500 - £1000 PER POLICY REQUIRED</span></div>
  </div>
  <div class="col" style="left:130px;top:62px">
    <div class="item"><h3>TITLES AND LAND ACQUISITION</h3><p>Budget for this item early, compare at least two written quotes and agree the scope in writing before any work begins on site.</p><span class="cost">EXPECTED COST: £1100 - £3000 IN SOLICITOR'S FEES</span></div>
    <div class="item"><h3>LAND OWNERS LIABILITY INSURANCE</h3><p>Budget for this item early, compare at least two written quotes and agree the scope in writing before any work begins on site.</p><span class="cost">EXPECTED COST: £50 - £150</span></div>
    <div class="item"><h3>PLANNING CONSULTANT</h3><p>Budget for this item early, compare at least two written quotes and agree the scope in writing before any work begins on site.</p><span class="cost">EXPECTED COST: £1500 - £3000</span></div>
    <div class="item"><h3>ARBORICULTURAL CONSULTANT</h3><p>Budget for this item early, compare at least two written quotes and agree the scope in writing before any work begins on site.</p><span class="cost">EXPECTED COST: £300 - £500</span></div>
  </div>
  <div class="abs inner1__photo" role="img" aria-label="Yellow site dumper truck cut out on white"></div>
  <div class="abs brand inner1__brand"><div class="brand__mark"></div><div class="brand__name">HARBOURLINE BUILDERS</div></div>
</section>

<!-- INNER PAGE 2 -->
<section class="page page--inner2">
  <div class="abs inner2__photo" role="img" aria-label="Site workers in hi-vis beside yellow dumpers on a building site"></div>
  <div class="col" style="left:6px;top:82px">
    <div class="item"><h3>COMMUNITY INFRASTRUCTURE LEVY</h3><p>Budget for this item early, compare at least two written quotes and agree the scope in writing before any work begins on site.</p><span class="cost cost--navy">EXPECTED COST: £400 - £1500</span></div>
    <div class="item"><h3>PLANNING PERMISSION</h3><p>Budget for this item early, compare at least two written quotes and agree the scope in writing before any work begins on site.</p><span class="cost cost--navy">EXPECTED COST: £400 - £1500</span></div>
    <div class="item"><h3>PLANNING PERMISSION</h3><p>Budget for this item early, compare at least two written quotes and agree the scope in writing before any work begins on site.</p><span class="cost cost--navy">EXPECTED COST: £462 FOR A SINGLE DWELLING + £230 - £300 FOR A PRE APP MEETING</span></div>
    <div class="item"><h3>COMMUNITY INFRASTRUCTURE LEVY</h3><p>Budget for this item early, compare at least two written quotes and agree the scope in writing before any work begins on site.</p><span class="cost cost--navy">EXPECTED COST: £400 - £1500</span></div>
  </div>
  <div class="col" style="left:130px;top:84px">
    <div style="text-align:center"><span class="section-tag">BROKER COST</span></div>
    <div class="item"><p>Budget for this item early, compare at least two written quotes and agree the scope in writing before any work begins on site.</p><span class="cost">EXPECTED COST: £500 - £3000</span></div>
    <div class="item"><h3>FINANCE</h3><p>Budget for this item early, compare at least two written quotes and agree the scope in writing before any work begins on site.</p><span class="cost cost--navy">EXPECTED COST: AROUND 0.7-1.2% A MONTH + FEES 1.0% ON THE AMOUNT TO BE BORROWED</span></div>
    <div class="item"><h3>QUANTITY SURVEYOR MONITORING FEES</h3><p>Budget for this item early, compare at least two written quotes and agree the scope in writing before any work begins on site.</p><span class="cost cost--navy">EXPECTED COST: £500 - £750 + VAT PER MONTHLY VISIT X LENGTH OF JOB</span></div>
    <div class="item"><h3>BUILDING REGULATION DRAWINGS</h3><p>Budget for this item early, compare at least two written quotes and agree the scope in writing before any work begins on site.</p><span class="cost cost--navy">EXPECTED COST: £1000 - £3000</span></div>
  </div>
  <div class="abs footer">www.harbourlinebuilders.co.uk</div>
</section>

<!-- BACK -->
<section class="page page--back">
  <div class="abs back__frame"></div>
  <p class="abs back__lead">For a construction partner, a joint venture, a builder or a straightforward sale, please call</p>
  <div class="abs back__name">OWEN MARSH ON</div>
  <div class="abs back__phone">07700 900418</div>
  <div class="abs back__mail">or email- owen@harbourline-mail.example</div>
  <div class="abs back__web">www.harbourlinebuilders.co.uk</div>
  <div class="abs brand back__brand">
    <div class="brand__mark"></div>
    <div class="brand__name">HARBOURLINE BUILDERS</div>
  </div>
</section>

<div class="caption" style="left:40px">COVER PAGE</div>
<div class="caption" style="left:345px">INNER PAGE1</div>
<div class="caption" style="left:620px">INNERPAGE-2</div>
<div class="caption" style="left:880px">BACK PAGE</div>

</body>
</html>
```